Corvanel Business card

I got my logo so I need to have that on my business card!!

Thanks
Updates

Reason: Hi designers, i will be deciding my logo by this weekend!!! As soon as I decide i will post my logo for your application Thanks Fedorico

I Just sent my logo for your attention!!!

Target Market(s)

My costumers will be enginners from shipyard industry!

Industry/Entity Type

Business

Requirements
Must have
• My future logo

```html
<!DOCTYPE html>
<html lang="en">
<head>
<meta charset="UTF-8">
<title>Corvanel Business Card – Front and Back</title>
<link rel="stylesheet" href="https://fonts.googleapis.com/css2?family=Poiret+One&family=Open+Sans:wght@400&family=Great+Vibes&display=swap">
<style>
  :root {
    --backdrop: #f3eec4;
    --card: #e6e6e8;
    --steel: #a7a8ab;
    --steel-light: #bcbdc0;
    --sand: #e3dccb;
    --tab: #e5dccb;
    --tab-hole: #d3c8b0;
    --ink: #111111;
    --white: #f4f4f5;
  }
  html, body {
    margin: 0;
    padding: 0;
    width: 1200px;
    height: 1000px;
    overflow: hidden;
    background: var(--backdrop);
  }
  .canvas {
    position: relative;
    width: 1200px;
    height: 1000px;
  }
  .side-tab {
    position: absolute;
    top: 145px;
    width: 230px;
    height: 105px;
    background: var(--tab);
    box-shadow: 3px 3px 6px rgba(0,0,0,0.18);
  }
  .side-tab__holes {
    position: absolute;
    top: 6px;
    left: 0;
    width: 230px;
    height: 16px;
  }
  .side-tab__label {
    position: absolute;
    left: 0;
    right: 0;
    top: 42px;
    text-align: center;
    font-family: "Great Vibes", cursive;
    font-size: 40px;
    color: var(--ink);
    font-weight: 700;
    -webkit-text-stroke: 0.6px var(--ink);
  }
  .tab-front { left: 130px; }
  .tab-back { left: 567px; }

  .card {
    position: absolute;
    top: 250px;
    width: 349px;
    height: 561px;
    background: var(--card);
    overflow: hidden;
  }
  .card-front { left: 67px; }
  .card-back { left: 504px; }
  .card__shapes {
    position: absolute;
    inset: 0;
    width: 349px;
    height: 561px;
  }
  .logo-placeholder {
    position: absolute;
    top: 32px;
    left: 0;
    right: 0;
    text-align: center;
    font-family: "Poiret One", sans-serif;
    font-size: 31px;
    line-height: 40px;
    letter-spacing: 0.5px;
  }
  .card-front .logo-placeholder { color: var(--card); }
  .card-back .logo-placeholder { color: var(--steel); }

  .holder-name {
    position: absolute;
    top: 363px;
    left: 0;
    right: 0;
    text-align: center;
    font-family: "Poiret One", sans-serif;
    font-size: 45px;
    line-height: 52px;
    color: var(--steel);
  }
  .holder-title {
    position: absolute;
    top: 416px;
    left: 0;
    right: 0;
    text-align: center;
    font-family: "Open Sans", sans-serif;
    font-size: 27px;
    color: var(--steel);
  }

  .contact-list {
    position: absolute;
    left: 8px;
    top: 430px;
    margin: 0;
    padding: 0;
    list-style: none;
  }
  .contact-list__item {
    display: flex;
    align-items: center;
    height: 40px;
    font-family: "Open Sans", sans-serif;
    font-size: 22px;
    letter-spacing: 1px;
    color: var(--white);
  }
  .contact-list__icon {
    width: 32px;
    height: 30px;
    margin-right: 13px;
    flex: none;
  }
</style>
</head>
<body>
<main class="canvas">

  <div class="side-tab tab-front">
    <svg class="side-tab__holes" viewBox="0 0 230 16">
      <g fill="var(--tab-hole)">
        <circle cx="14" cy="8" r="6"/><circle cx="38" cy="8" r="6"/><circle cx="62" cy="8" r="6"/>
        <circle cx="86" cy="8" r="6"/><circle cx="110" cy="8" r="6"/><circle cx="134" cy="8" r="6"/>
        <circle cx="158" cy="8" r="6"/><circle cx="182" cy="8" r="6"/><circle cx="206" cy="8" r="6"/>
      </g>
    </svg>
    <div class="side-tab__label">Front</div>
  </div>

  <div class="side-tab tab-back">
    <svg class="side-tab__holes" viewBox="0 0 230 16">
      <g fill="var(--tab-hole)">
        <circle cx="14" cy="8" r="6"/><circle cx="38" cy="8" r="6"/><circle cx="62" cy="8" r="6"/>
        <circle cx="86" cy="8" r="6"/><circle cx="110" cy="8" r="6"/><circle cx="134" cy="8" r="6"/>
        <circle cx="158" cy="8" r="6"/><circle cx="182" cy="8" r="6"/><circle cx="206" cy="8" r="6"/>
      </g>
    </svg>
    <div class="side-tab__label">Back</div>
  </div>

  <section class="card card-front">
    <svg class="card__shapes" viewBox="0 0 349 561">
      <polygon fill="var(--sand)" points="0,0 349,0 349,160 175,287 0,160"/>
      <polygon fill="var(--steel-light)" points="0,0 349,0 349,140 175,267 0,140"/>
      <polygon fill="var(--steel)" points="0,0 349,0 349,120 175,247 0,120"/>
    </svg>
    <div class="logo-placeholder">Your<br>Future<br>Logo</div>
    <div class="holder-name">YOUR NAME</div>
    <div class="holder-title">Title</div>
  </section>

  <section class="card card-back">
    <svg class="card__shapes" viewBox="0 0 349 561">
      <polygon fill="var(--sand)" points="0,350 175,180 349,350 349,561 0,561"/>
      <polygon fill="var(--steel-light)" points="0,378 175,208 349,378 349,561 0,561"/>
      <polygon fill="var(--steel)" points="0,405 175,234 349,405 349,561 0,561"/>
    </svg>
    <div class="logo-placeholder">Your<br>Future<br>Logo</div>
    <ul class="contact-list">
      <li class="contact-list__item">
        <svg class="contact-list__icon" viewBox="0 0 32 30">
          <polygon fill="var(--white)" points="16,2 1,15 5,15 5,28 13,28 13,20 19,20 19,28 27,28 27,15 31,15"/>
          <rect fill="var(--white)" x="22" y="4" width="4" height="7"/>
        </svg>
        Your Address
      </li>
      <li class="contact-list__item">
        <svg class="contact-list__icon" viewBox="0 0 32 30">
          <circle cx="16" cy="15" r="13" fill="none" stroke="var(--white)" stroke-width="2"/>
          <path fill="var(--white)" d="M11 8 C9 10 9 14 12 18 C15 22 19 23 21 22 L22 19 L19 17 L17 19 C15 18 13 15 13 13 L15 12 L14 8 Z"/>
        </svg>
        Telephone
      </li>
      <li class="contact-list__item">
        <svg class="contact-list__icon" viewBox="0 0 32 30">
          <rect x="3" y="7" width="26" height="17" fill="none" stroke="var(--white)" stroke-width="2"/>
          <polyline points="3,7 16,18 29,7" fill="none" stroke="var(--white)" stroke-width="2"/>
          <line x1="3" y1="24" x2="13" y2="15" stroke="var(--white)" stroke-width="2"/>
          <line x1="29" y1="24" x2="19" y2="15" stroke="var(--white)" stroke-width="2"/>
        </svg>
        Email
      </li>
    </ul>
  </section>

</main>
</body>
</html>
```